Clean/luxurious/food site. Work should be completed this weekend

Project Description:
This is a flash work. The design must be clean and ready by the end of the weekend.
I will provide full 24hr support to give feedback and get it ready.
Final product must be the final PSD files with all the design blocks, complete CSS, and links programed into the files.
The work is simple and straight forward, the design structure should be just the 5 elements presented.
What do you do?
The basic idea: We are a highend catering platform.
We provide a better way to discover, compare, and order catering from local restaurants, high end caterers, and chefs.

The basic platform structure
Each Caterer will have a simple and clean profile page which will contain
• Basic details of the Caterer
1. Purveyor
2. Cuisine
3. Amount of Food
4. Price Per Person
5. Min Order
6. Max Order
7. Notice Required
ORDER BOX- where users decide the amount of the order base on the # of people and price per person

• Slideshow for picture of food provided (max 5 pictures)
• A short text box for the description of the food and the delivery options
• The feedback that the caterer has received from clients
• Basic badge system (based on the 5 star rating)

The SITE WILL BE IN SPANISH. Our target market is found in Latinamerica
Do you have a desired website screen size?
Full screen ( optimized for a 13 Inch screen)
How many pages (maximum of 5) do you need designed?
5 pages (1- Landing page) (2-Signup process (max 3 step signup process) (3-Caterer individual profile page) (4-Search page) (5-Static page Full left sidebar)
What is your industry?
We are in the restaurant, food and luxury high end industry
Describe the target audience for your website design
Site will be in spanish. Target audience in LatinAmerica.. age 16-29, women, urban, speak Spanish and English are active on social networks and like extracurricular activities.

What 3 things would you like to communicate to your audience through your website design
Find great private catarers
The best food in town
Simple and secure
Clean
The best match
How is your company different from your competitors?
Clean simple design to search by date or reference the best match
Free service
Luxurious touch
backed by the best on the industry
What website design styles do you like?
Inspiration for Landing Page
http://plantuvo.com/

The concept

https://www.mealbrisk.com/

The landing page
http://plantuvo.com/

The signup for chefs
https://www.tavrino.com/chef_applications/new
https://www.mealbrisk.com/packages/new

The inner pages

https://www.mealbrisk.com/collections/11-personal-touch
QuelVane.com https://www.tavrino.com/

What colors do you want to see in your website design?
•Different types of blue (light blue) or orange
No more than 2 colors
white/earth
light green
• Use the codlark fromtwitter scaffold design (http://chirvox.codlark.com/scaffold/)
What colors do you NOT want to see in your website design?
Black-pink-red-yellow
What adjectives should best describe your website design?
clean
bold
bright
texture
What content must be included in the website design?
landing page with no more than 3 elements, very clean and simple
Landing page should have either have a central space for main tagline or a broken 2 sided box must have a bottom footer to have the basic navigation links (like quelvane.com)
Use of simple and clean icons
Top right space for small logo
Use of helvetica or clean modern font
inner pages with a simple structure and a left sidebar to add a few elements of navigation
inner pages should have an upper slim banner for navigation bar or breadcrumbs
Do you have additional requirements or links you want to share?
• Use the codlark from chirvox scaffold design (http://chirvox.codlark.com/scaffold/)

ONLY SERIOUS ABOUT DESIGN AND FINISH THIS WEEKEND

```html
<!DOCTYPE html>
<html lang="en">
<head>
<meta charset="utf-8">
<title>Our Caterers</title>
<link href="https://fonts.googleapis.com/css2?family=Lobster&family=Lobster+Two:ital,wght@0,400;1,400&family=Questrial&family=Open+Sans:wght@400;600&display=swap" rel="stylesheet">
<style>
  :root {
    --green: #8aa46e;
    --green-dark: #4a6a2c;
    --green-btn: #94b47a;
    --header-band: #9bb77e;
    --panel-bg: #f6f6f3;
    --card-bg: #ffffff;
    --card-head: #e2e2e1;
    --card-border: #cfcfcc;
    --ink: #3d3d33;
    --ink-soft: #55554a;
    --star: #555550;
    --footer-bg: #3f3b27;
    --white: #ffffff;
  }
  * { box-sizing: border-box; margin: 0; padding: 0; }
  html, body { width: 1200px; height: 800px; overflow: hidden; }
  body {
    position: relative;
    font-family: "Open Sans", sans-serif;
    color: var(--ink);
  }
  .backdrop {
    position: absolute; inset: 0;
    background:
      radial-gradient(ellipse 420px 300px at 1130px 130px, rgba(255,240,200,.9), transparent 70%),
      radial-gradient(ellipse 300px 260px at 1100px 460px, rgba(150,95,45,.85), transparent 75%),
      linear-gradient(90deg, #2f261d 0%, #4b3d2f 10%, #b8b3ab 28%, #d8d5d0 50%, #d2cec6 70%, #8c6b47 88%, #3e2a1b 100%);
  }
  .site-header {
    position: absolute; left: 0; top: 0; width: 1200px; height: 82px;
    background: linear-gradient(90deg, #a3bd86 0%, #8fab72 35%, #a6bf8a 65%, #93ae77 100%);
    box-shadow: 0 2px 6px rgba(0,0,0,.35);
  }
  .brand {
    position: absolute; left: 144px; top: 12px;
    font-family: "Lobster", cursive; font-size: 46px; color: var(--white);
  }
  .header-links { position: absolute; top: 16px; right: 190px; display: flex; gap: 26px; }
  .header-link {
    display: flex; flex-direction: column; align-items: center;
    font-family: "Questrial", sans-serif; font-size: 16px; color: var(--white);
    text-decoration: none;
  }
  .header-link svg { width: 30px; height: 30px; margin-bottom: 4px; }

  .caterers-panel {
    position: absolute; left: 111px; top: 108px; width: 969px; height: 496px;
    background: var(--panel-bg); border-radius: 3px;
    box-shadow: 0 2px 8px rgba(0,0,0,.35);
  }
  .panel-title {
    height: 52px; background: var(--green); border-radius: 3px 3px 0 0;
    font-family: "Lobster", cursive; font-size: 24px; color: var(--white);
    text-align: center; line-height: 52px;
  }
  .caterer-card {
    position: absolute; top: 76px; width: 456px; height: 357px;
    background: var(--card-head); border: 1px solid var(--card-border); border-radius: 3px;
  }
  .caterer-card.first { left: 18px; }
  .caterer-card.second { left: 494px; }
  .card-name {
    height: 33px; line-height: 33px; text-align: center;
    font-family: "Lobster", cursive; font-size: 15px; color: var(--green-dark);
    border-bottom: 1px solid var(--card-border);
  }
  .card-body { position: absolute; left: 1px; right: 1px; top: 33px; height: 248px; background: var(--card-bg); }
  .detail {
    position: absolute; font-family: "Lobster Two", cursive; font-style: italic;
    font-size: 10px; color: var(--ink); white-space: nowrap;
  }
  .detail b {
    font-family: "Lobster", cursive; font-weight: 400; font-style: normal;
    font-size: 12px; color: var(--green-dark); display: inline-block;
  }
  .detail.left b { width: 68px; }
  .detail.left b.short { width: auto; }
  .detail.right b { width: 74px; }
  .slideshow {
    position: absolute; left: 32px; top: 53px; width: 181px; height: 116px;
    border: 3px solid var(--white); box-shadow: 0 0 3px rgba(0,0,0,.35);
    background: linear-gradient(120deg, #b2582a 0%, #d7a25f 30%, #6e8a3a 60%, #c8bfb0 100%);
  }
  .slide-dots {
    position: absolute; left: 0; right: 0; bottom: 0; height: 12px;
    background: rgba(40,40,30,.55); display: flex; justify-content: center; align-items: center; gap: 3px;
  }
  .slide-dots span { width: 5px; height: 5px; border-radius: 50%; background: #e8e8e8; }
  .slide-dots span.active { background: #e5873f; }
  .note {
    position: absolute; left: 32px; width: 180px;
    font-family: "Lobster Two", cursive; font-style: italic; font-size: 9.5px; line-height: 12px; color: var(--ink);
  }
  .feedback-title {
    position: absolute; left: 241px; top: 109px;
    font-family: "Lobster", cursive; font-size: 12px; color: var(--green-dark); text-decoration: underline;
  }
  .feedback {
    position: absolute; left: 241px; width: 182px;
    font-family: "Lobster Two", cursive; font-style: italic; font-size: 9.5px; line-height: 12px; color: var(--ink);
  }
  .rating { position: absolute; left: 241px; top: 221px; display: flex; align-items: center; }
  .rating b { font-family: "Lobster", cursive; font-weight: 400; font-size: 12px; color: var(--green-dark); margin-right: 10px; }
  .rating svg { width: 14px; height: 14px; margin-right: 4.5px; fill: var(--star); }
  .order-box { position: absolute; left: 0; right: 0; top: 282px; bottom: 0; }
  .order-title {
    position: absolute; left: 33px; top: 12px;
    font-family: "Lobster", cursive; font-size: 15px; color: var(--green-dark); text-decoration: underline;
  }
  .order-input {
    position: absolute; top: 37px; width: 152px; height: 25px;
    background: var(--white); border: 1px solid #c8c8c4;
    font-family: "Open Sans", sans-serif; font-size: 10px; color: #8a8a85;
    padding-left: 7px; line-height: 23px;
  }
  .order-input.item { left: 32px; }
  .order-input.qty { left: 191px; }
  .submit {
    position: absolute; left: 355px; top: 37px; width: 64px; height: 24px;
    background: linear-gradient(#a7c38d, #88a86c); border: 1px solid #7d9c62; border-radius: 2px;
    font-family: "Open Sans", sans-serif; font-size: 11px; color: var(--white);
    text-align: center; line-height: 22px;
  }
  .pager {
    position: absolute; left: 0; right: 0; bottom: 0; height: 34px;
    border-top: 1px solid #d6d6d2; background: #f0f0ed; border-radius: 0 0 3px 3px;
  }
  .pager-btn {
    position: absolute; top: 4px; width: 24px; height: 24px;
    background: var(--white); border: 1px solid #c8c8c4; border-radius: 2px;
  }
  .pager-btn svg { width: 22px; height: 22px; }
  .pager-btn.prev { left: 457px; }
  .pager-btn.next { left: 490px; }
  .page-count {
    position: absolute; right: 22px; top: 7px;
    font-family: "Open Sans", sans-serif; font-size: 15px; color: #5a5a55;
  }
  .dish-strip { position: absolute; top: 626px; left: 428px; display: flex; gap: 14px; }
  .dish {
    width: 63px; height: 63px; border-radius: 50%; border: 2px solid #eeeeea;
    box-shadow: 0 1px 4px rgba(0,0,0,.5);
  }
  .dish.d1 { background: radial-gradient(circle, #8b5a36, #3b2a1c); }
  .dish.d2 { background: radial-gradient(circle, #6b3a22, #c9a98a); }
  .dish.d3 { background: radial-gradient(circle, #6d7a3a, #2a1c14); }
  .dish.d4 { background: radial-gradient(circle, #c2955e, #e8e2d8); }
  .dish.d5 { background: radial-gradient(circle, #d9d2c2, #a36a3a); }
  .site-footer {
    position: absolute; left: 0; bottom: 0; width: 1200px; height: 86px;
    background: linear-gradient(#45402b, #3a3623);
  }
  .footer-nav a {
    position: absolute; top: 19px; font-family: "Questrial", sans-serif; font-size: 17px;
    color: var(--white); text-decoration: none;
  }
  .footer-nav a.current { text-decoration: underline; }
  .copyright {
    position: absolute; left: 0; right: 0; top: 50px; text-align: center;
    font-family: "Questrial", sans-serif; font-style: italic; font-size: 14px; color: var(--white);
  }
</style>
</head>
<body>
  <div class="backdrop" role="img" aria-label="Blurred photo of a plated dish on a table"></div>

  <header class="site-header">
    <div class="brand">Logo</div>
    <nav class="header-links">
      <a class="header-link" href="#">
        <svg viewBox="0 0 30 30" fill="none" stroke="#ffffff" stroke-width="1.6"><circle cx="15" cy="9" r="6"/><path d="M5 28c0-7 4-11 10-11s10 4 10 11z"/></svg>
        User Login
      </a>
      <a class="header-link" href="#">
        <svg viewBox="0 0 30 30" fill="none" stroke="#ffffff" stroke-width="1.6"><path d="M3 4h24v16H14l-6 6v-6H3z"/><path d="M8 10h14M8 14h10"/></svg>
        Speak Us
      </a>
    </nav>
  </header>

  <main class="caterers-panel">
    <h1 class="panel-title">Our Caterers</h1>

    <article class="caterer-card first">
      <h2 class="card-name">Caterers Name</h2>
      <div class="card-body">
        <p class="detail left" style="left:32px;top:10px"><b class="short">Surveyor Name</b> : ABC Caterer, CA</p>
        <p class="detail left" style="left:32px;top:30px"><b>Cuisine Name</b> : Title goes here</p>
        <div class="slideshow" role="img" aria-label="Slideshow photo of catered finger food">
          <div class="slide-dots"><span></span><span class="active"></span><span></span><span></span><span></span></div>
        </div>
        <p class="note" style="top:177px">Food description goes here. Put some text here about this item.</p>
        <p class="note" style="top:221px;width:200px">Delivery Option goes here : Put some text here.</p>
        <p class="detail right" style="left:241px;top:10px"><b>Amount of Food</b> : Put amt. here</p>
        <p class="detail right" style="left:241px;top:30px"><b>Price Per Person</b> : USD 25 P. Prsn.</p>
        <p class="detail right" style="left:241px;top:49px"><b>Min Order</b> : 4 Items</p>
        <p class="detail right" style="left:241px;top:69px"><b>Max Order</b> : 50 Items</p>
        <p class="detail right" style="left:241px;top:89px"><b>Notice Required</b> : Min One Official Day</p>
        <p class="feedback-title">Customer's feedback</p>
        <p class="feedback" style="top:128px">Just to say about this caterer, the awsome food i had ever taste any kind of this cuisine.</p>
        <p class="feedback" style="top:157px">Just to say about this caterer, the awsome food i had ever taste any kind of this cuisine.</p>
        <p class="feedback" style="top:187px">Just to say about this caterer, the awsome food i had ever taste any kind of this cuisine.</p>
        <div class="rating"><b>Rate this caterer :</b>
          <svg viewBox="0 0 24 24"><polygon points="12,1 15,9 23,9 17,14 19,23 12,18 5,23 7,14 1,9 9,9"/></svg>
          <svg viewBox="0 0 24 24"><polygon points="12,1 15,9 23,9 17,14 19,23 12,18 5,23 7,14 1,9 9,9"/></svg>
          <svg viewBox="0 0 24 24"><polygon points="12,1 15,9 23,9 17,14 19,23 12,18 5,23 7,14 1,9 9,9"/></svg>
          <svg viewBox="0 0 24 24"><polygon points="12,1 15,9 23,9 17,14 19,23 12,18 5,23 7,14 1,9 9,9"/></svg>
          <svg viewBox="0 0 24 24"><polygon points="12,1 15,9 23,9 17,14 19,23 12,18 5,23 7,14 1,9 9,9"/></svg>
        </div>
      </div>
      <div class="order-box">
        <p class="order-title">Order Now</p>
        <div class="order-input item">Item Name</div>
        <div class="order-input qty">Nos. of item</div>
        <div class="submit">Submit</div>
      </div>
    </article>

    <article class="caterer-card second">
      <h2 class="card-name">Caterers Name</h2>
      <div class="card-body">
        <p class="detail left" style="left:32px;top:10px"><b class="short">Surveyor Name</b> : ABC Caterer, CA</p>
        <p class="detail left" style="left:32px;top:30px"><b>Cuisine Name</b> : Title goes here</p>
        <div class="slideshow" role="img" aria-label="Slideshow photo of catered finger food">
          <div class="slide-dots"><span></span><span class="active"></span><span></span><span></span><span></span></div>
        </div>
        <p class="note" style="top:177px">Food description goes here. Put some text here about this item.</p>
        <p class="note" style="top:221px;width:200px">Delivery Option goes here : Put some text here.</p>
        <p class="detail right" style="left:241px;top:10px"><b>Amount of Food</b> : Put amt. here</p>
        <p class="detail right" style="left:241px;top:30px"><b>Price Per Person</b> : USD 25 P. Prsn.</p>
        <p class="detail right" style="left:241px;top:49px"><b>Min Order</b> : 4 Items</p>
        <p class="detail right" style="left:241px;top:69px"><b>Max Order</b> : 50 Items</p>
        <p class="detail right" style="left:241px;top:89px"><b>Notice Required</b> : Min One Official Day</p>
        <p class="feedback-title">Customer's feedback</p>
        <p class="feedback" style="top:128px">Just to say about this caterer, the awsome food i had ever taste any kind of this cuisine.</p>
        <p class="feedback" style="top:157px">Just to say about this caterer, the awsome food i had ever taste any kind of this cuisine.</p>
        <p class="feedback" style="top:187px">Just to say about this caterer, the awsome food i had ever taste any kind of this cuisine.</p>
        <div class="rating"><b>Rate this caterer :</b>
          <svg viewBox="0 0 24 24"><polygon points="12,1 15,9 23,9 17,14 19,23 12,18 5,23 7,14 1,9 9,9"/></svg>
          <svg viewBox="0 0 24 24"><polygon points="12,1 15,9 23,9 17,14 19,23 12,18 5,23 7,14 1,9 9,9"/></svg>
          <svg viewBox="0 0 24 24"><polygon points="12,1 15,9 23,9 17,14 19,23 12,18 5,23 7,14 1,9 9,9"/></svg>
          <svg viewBox="0 0 24 24"><polygon points="12,1 15,9 23,9 17,14 19,23 12,18 5,23 7,14 1,9 9,9"/></svg>
          <svg viewBox="0 0 24 24"><polygon points="12,1 15,9 23,9 17,14 19,23 12,18 5,23 7,14 1,9 9,9"/></svg>
        </div>
      </div>
      <div class="order-box">
        <p class="order-title">Order Now</p>
        <div class="order-input item">Item Name</div>
        <div class="order-input qty">Nos. of item</div>
        <div class="submit">Submit</div>
      </div>
    </article>

    <div class="pager">
      <div class="pager-btn prev"><svg viewBox="0 0 22 22"><polygon points="15,5 15,17 6,11" fill="#333"/></svg></div>
      <div class="pager-btn next"><svg viewBox="0 0 22 22"><polygon points="7,5 7,17 16,11" fill="#333"/></svg></div>
      <p class="page-count">Page 1 of 25</p>
    </div>
  </main>

  <div class="dish-strip">
    <div class="dish d1" role="img" aria-label="Photo of a sandwich"></div>
    <div class="dish d2" role="img" aria-label="Photo of a chocolate cake slice"></div>
    <div class="dish d3" role="img" aria-label="Photo of a salad"></div>
    <div class="dish d4" role="img" aria-label="Photo of a plated dessert"></div>
    <div class="dish d5" role="img" aria-label="Photo of sushi rolls"></div>
  </div>

  <footer class="site-footer">
    <nav class="footer-nav">
      <a href="#" style="left:344px">Home</a>
      <a href="#" style="left:439px">What we do</a>
      <a href="#" class="current" style="left:577px">Caterers</a>
      <a href="#" style="left:691px">Menu</a>
      <a href="#" style="left:778px">Contact Us</a>
    </nav>
    <p class="copyright">Copyright@2012 &nbsp;|&nbsp; Privacy Plicy</p>
  </footer>
</body>
</html>
```